July 2022 Industrial Manufacturer Product Expo Mexico City

We manufacture large screws and fastners for large Mining equipment, Trains, large ships, airplanes, wind turbines, and so on. We also do custom work base on the customer needs. No matter the size we can make it.
We have a Expo coming up with companies all over the world. We have to stand out we are a family own business so our customer service will be above and beyond anyone can provide. We do not have a sales force to push our products and services we provide one on one service.
Plus@!! I'm looking for anything that you designers can come up with if it was your company to put on a business card, plus i want to do a 1 or 2 sided pamphlet, and then a website. We make Speciality Bolts for large mining equipment these bolts can be 3 to 4 foot long!!! Plus fasteners, Nuts, washers, any, size, strengths, special materials, we offer more of a ono on one customer service, We are a small company, family own, but can fulfill any type of orders. We can also provide special time lines for emergency orders. "We keep the machines running we here at KRV don't believe in down time" We want to hear any slogan based on our company to stand out.
Thanks i really appreciate all your work and options that we have to pick on. Plus just a thought we could possibly want to entertain a experience Marketing internet help maybe a employment possibility. Thanks
Updates

I need 2 cards one in Spanish and English Like the steel back ground maybe send me in some bright red and blue writing Same with the Black cards Please remove the word Military The logo KRV maybe integrate a picture of a Bolt 🔩 Thank you

Still looking for I need 2 cards one in Spanish and English Like the steel back ground maybe send me in some bright red and blue writing Same with the Black cards try bright writing Please remove the word Military The logo KRV maybe integrate a picture of a Bolt 🔩 Plus will need the company to make a brochure and website next Thank you

Target Market(s)

Large Mining, Ship, Train, Green Energy, ORBA, and Government equipment. Throughout the World

Industry/Entity Type

We can Custom Manufacture any type of Fastners for Mining equipment, Trains, Ships, Green energy, Governments, or military projects. wind turbines,

Contact Information for Business Card

I attached the name and contact info that's on a card, plus the Company Logo. Would like industrial looking background with Bright Colors that will stand out!! If we can insert somewhere maybe on back that we "Custom Manufacture Any Size or Quantity Fastners for Large Mining Equipment, Trains, Ships, Green Energy Equipment or Government Projects

Font styles to use
Other font styles liked:
• You Pick, has to be bold, colorful standout, Professional looking Beable to read it.

Colors

Designer to choose colors to be used in the design.

Requirements
Must have
• Need in Spanish and English TO STANDOUT FROM THE REST OF THE EXPO!! See Business card details, Rounded corners
Nice to have
• Can i see some of the darker cards with Bright Red and Blue letters I like to see the different type of card material, heavy thickness, plastic, transparent, Metal types, Bright Colors, I saw like Raised letters like on the logo.

```html
<!DOCTYPE html>
<html lang="es">
<head>
<meta charset="utf-8">
<title>KRV – Tarjetas de presentación</title>
<link rel="stylesheet" href="https://fonts.googleapis.com/css2?family=Arimo:wght@400;700&display=swap">
<style>
  :root{
    --page:#e9e9ea;
    --card:#2c2c2e;
    --card-back:#262628;
    --pattern-a:#1e1e20;
    --pattern-b:#4a4a4d;
    --white:#ffffff;
    --blue:#1f63c9;
    --blue-deep:#173fa8;
    --rule:#9a9a9d;
  }
  *{box-sizing:border-box;margin:0;padding:0}
  html,body{width:1200px;height:802px;overflow:hidden}
  body{background:var(--page);font-family:"Arimo",Arial,sans-serif;position:relative}

  .card{
    position:absolute;width:540px;height:310px;border-radius:14px;
    box-shadow:0 10px 28px rgba(0,0,0,.22);overflow:hidden;
  }
  .card--front{left:70px;top:90px;background:var(--card);color:var(--white)}
  .card--back{left:590px;top:400px;background:var(--card-back)}

  .brand{
    position:absolute;left:0;right:0;top:56px;text-align:center;
    font-weight:700;font-size:92px;letter-spacing:6px;color:var(--white);line-height:1;
  }
  .brand-dot{
    display:inline-block;width:18px;height:18px;border-radius:50%;
    background:var(--blue);vertical-align:middle;margin-left:10px;
  }
  .tagline{
    position:absolute;left:0;right:0;top:164px;text-align:center;
    font-weight:700;font-size:14px;letter-spacing:.6px;
  }

  .contact{position:absolute;left:48px;right:30px;bottom:34px;display:flex;align-items:center}
  .person{width:200px;text-align:right;padding-right:18px}
  .person-name{color:var(--blue);font-weight:700;font-size:19px;line-height:1.15}
  .person-name--last{color:var(--blue-deep)}
  .person-role{font-size:15px;margin-top:4px}
  .divider{width:1px;height:78px;background:var(--rule)}
  .details{padding-left:16px;list-style:none;font-size:15px;line-height:1.45}
  .details li{display:flex;align-items:center;gap:7px}
  .details svg{width:13px;height:13px;flex:none}

  .back-pattern{position:absolute;inset:0;background:linear-gradient(120deg,var(--pattern-a) 0%,var(--card-back) 45%,var(--pattern-b) 100%)}
  .back-brand{
    position:absolute;right:110px;bottom:86px;font-weight:700;font-size:34px;
    letter-spacing:3px;color:var(--white);
  }
</style>
</head>
<body>

<section class="card card--front">
  <div class="brand">KRV<span class="brand-dot"></span></div>
  <p class="tagline">FABRICATION Y DISTRIBUTION DE TORNILLOS</p>

  <div class="contact">
    <div class="person">
      <p class="person-name">Lic. Marisol</p>
      <p class="person-name person-name--last">Ibarra Vela</p>
      <p class="person-role">Cotizaciones en</p>
    </div>
    <div class="divider"></div>
    <ul class="details">
      <li>
        <svg viewBox="0 0 16 16"><circle cx="8" cy="8" r="8" fill="#1f63c9"/><path d="M5.3 4.2l1.5 1.6-.8 1.1c.6 1.2 1.6 2.2 2.8 2.8l1.1-.8 1.6 1.5-.9 1.3c-3-.5-5.6-3.1-6.1-6.1z" fill="#fff"/></svg>
        8710042518
      </li>
      <li>
        <svg viewBox="0 0 16 16"><circle cx="8" cy="8" r="8" fill="#1f63c9"/><path d="M5.3 4.2l1.5 1.6-.8 1.1c.6 1.2 1.6 2.2 2.8 2.8l1.1-.8 1.6 1.5-.9 1.3c-3-.5-5.6-3.1-6.1-6.1z" fill="#fff"/></svg>
        8710367294
      </li>
      <li>
        <svg viewBox="0 0 16 16"><rect x="1" y="3" width="14" height="10" rx="1" fill="#1f63c9"/><path d="M1.5 3.8L8 8.6l6.5-4.8" fill="none" stroke="#fff" stroke-width="1.2"/></svg>
        ventas@krvtornillos.mx
      </li>
    </ul>
  </div>
</section>

<section class="card card--back">
  <div class="back-pattern" role="img" aria-label="Embossed repeating company name pattern in dark and light grey"></div>
  <p class="back-brand">KRV</p>
</section>

</body>
</html>
```